Mara Quintell Fitness

I need a web design for my nutrition/fitness training business. The name of the business is MQ Fitness. I sell fitness programs and do online personal training/nutritional coaching. What I promote right now is my 8 week program and i'm also coming out with a phase two 8 week program. I want to feature both, with paypal links that way people can buy it through my website. I want the website designed around my logo with a black background. And tabs for my program, a tab for an about me section, a tab for me to post a blog, and a tab for my client testimonials/transformations. I want it to be pretty simple and easy to navigate through.
Target Market(s)
Fitness Industry
Industry/Entity Type
Fitness
Number of Pages Required
5+ page
Requirements
Must have
- I made a mock design and put it in the images. I want my website front page to be focused on my logo (which I attached) and also the tabs shown like I have it. Also need a play under my 8 week program tab to let people purchase my separate programs with paypal. Under the blog I just need something that says "coming soon" on that page. And under the about me I attached a picture of my that I want (eating a donut lol) where I want to be able to put a bio next to it.

```html
<!DOCTYPE html>
<html lang="en">
<head>
<meta charset="utf-8">
<title>MQ Fitness</title>
<link href="https://fonts.googleapis.com/css2?family=Oswald:wght@400;500&family=Open+Sans:wght@400;600;700&display=swap" rel="stylesheet">
<style>
:root{
  --black:#0d0d0d;
  --dark:#1b1b1b;
  --panel:#262626;
  --green:#7cc242;
  --green-dark:#1f3a12;
  --green-deep:#15280c;
  --white:#ffffff;
  --grey:#b9b9b9;
  --text-dark:#444;
}
*{margin:0;padding:0;box-sizing:border-box}
html,body{width:1200px;height:2224px;overflow:hidden;background:var(--black)}
body{font-family:"Open Sans",Arial,sans-serif;color:var(--white);position:relative}
.abs{position:absolute}

/* header */
.site-header{left:0;top:0;width:1200px;height:80px;background:var(--black)}
.brand{left:82px;top:14px;display:flex;align-items:center;gap:12px}
.brand-dot{width:44px;height:44px;border-radius:50%;background:var(--green)}
.brand-name{font-family:"Oswald",sans-serif;font-weight:500;font-size:30px;color:var(--green);letter-spacing:1px}
.main-nav{right:80px;top:0;height:80px;display:flex;align-items:center;gap:30px}
.main-nav a{font-family:"Oswald",sans-serif;font-size:15px;color:var(--white);text-decoration:none;letter-spacing:.5px;padding:28px 0 26px}
.main-nav a.active{color:var(--green);border-bottom:3px solid var(--green)}

/* hero */
.hero{left:0;top:80px;width:1200px;height:640px;background:linear-gradient(100deg,#6a5543 0%,#a58a6c 30%,#cdb79b 55%,#d9c9b1 75%,#bfa88d 100%)}
.hero-title{right:130px;top:390px;font-family:"Oswald",sans-serif;font-weight:500;font-size:70px;color:#262019;letter-spacing:1px}
.hero-sub{right:130px;top:480px;font-family:"Oswald",sans-serif;font-size:28px;color:var(--green);letter-spacing:1px}
.hero-arrow{top:390px;width:40px;height:40px}
.hero-arrow.prev{left:44px}
.hero-arrow.next{right:44px}

/* welcome */
.welcome{left:0;top:720px;width:1200px;height:220px;background:linear-gradient(180deg,var(--green-dark),var(--green-deep));text-align:center;padding-top:38px}
.welcome h2{font-family:"Oswald",sans-serif;font-weight:500;font-size:32px;letter-spacing:1px}
.welcome h2 span{color:var(--green)}
.welcome p{width:1020px;margin:20px auto 0;font-size:14px;line-height:22px;color:#d8e2d0}

/* programs */
.programs{left:0;top:940px;width:1200px;height:480px;background:linear-gradient(180deg,#141414,#2a2a2a)}
.program{top:70px;width:336px}
.program-photo{width:336px;height:196px;border:4px solid var(--white)}
.program h3{margin-top:22px;font-family:"Oswald",sans-serif;font-weight:500;font-size:18px;color:var(--green)}
.program p{margin-top:8px;font-size:13px;line-height:20px;color:var(--grey);width:300px}
.btn{display:inline-block;margin-top:16px;background:var(--green);color:var(--white);font-size:13px;font-weight:600;padding:7px 18px;border-radius:3px;border:1px solid #5d9a2c}

/* about */
.about{left:0;top:1420px;width:1200px;height:370px;background:linear-gradient(180deg,#3a3a3a,#1e1e1e)}
.about-photo{left:86px;top:40px;width:348px;height:300px;border:4px solid var(--white)}
.about-card{left:434px;top:52px;width:690px;height:278px;background:var(--white);padding:28px 34px}
.about-card h2{font-family:"Oswald",sans-serif;font-weight:500;font-size:30px;color:var(--green)}
.about-card p{margin-top:14px;font-size:13px;line-height:21px;color:var(--text-dark)}

/* blog */
.blog{left:0;top:1790px;width:1200px;height:300px;background:linear-gradient(180deg,#242424,#0f0f0f)}
.blog h2{left:84px;top:28px;font-family:"Oswald",sans-serif;font-weight:500;font-size:26px}
.blog-arrows{right:84px;top:36px;display:flex;gap:8px}
.post{top:82px;display:flex;gap:20px}
.post-photo{width:232px;height:150px;border:4px solid var(--white)}
.post-body{width:230px;padding-top:4px}
.post-body h3{font-family:"Oswald",sans-serif;font-weight:500;font-size:15px}
.post-date{font-size:12px;color:var(--green);margin-top:4px}
.post-body p{font-size:12px;line-height:18px;color:var(--grey);margin-top:6px}
.post-more{font-size:12px;color:var(--white);margin-top:8px;font-weight:600}

/* footer */
.site-footer{left:0;top:2090px;width:1200px;height:134px;background:var(--black)}
.footer-links{left:84px;top:46px;font-size:12px;color:var(--white)}
.copyright{left:84px;top:68px;font-size:12px;color:var(--grey)}
.footer-right{right:84px;top:44px;display:flex;gap:8px;align-items:center}
.pay-badge{width:80px;height:30px;background:#f2c14e;border-radius:4px}
.social{width:28px;height:28px;border-radius:3px}
.social.s1{background:#3b5998}.social.s2{background:#c4302b}.social.s3{background:#2aa9e0}.social.s4{background:#0e76a8}.social.s5{background:#3b5998}
</style>
</head>
<body>

<header class="site-header abs">
  <div class="brand abs"><span class="brand-dot"></span><span class="brand-name">MQ Fitness</span></div>
  <nav class="main-nav abs">
    <a class="active">HOME</a><a>ABOUT MARA</a><a>MY 8 WEEK PROGRAM</a><a>BLOG</a><a>TRANSFORMATIONS</a><a>CONTACT US</a>
  </nav>
</header>

<section class="hero abs" role="img" aria-label="Athlete lifting a dumbbell in a gym">
  <svg class="hero-arrow prev abs" viewBox="0 0 40 40"><circle cx="20" cy="20" r="19" fill="rgba(0,0,0,.35)"/><path d="M23 12l-8 8 8 8" stroke="#fff" stroke-width="3" fill="none"/></svg>
  <svg class="hero-arrow next abs" viewBox="0 0 40 40"><circle cx="20" cy="20" r="19" fill="rgba(0,0,0,.35)"/><path d="M17 12l8 8-8 8" stroke="#fff" stroke-width="3" fill="none"/></svg>
  <div class="hero-title abs">MQ FITNESS</div>
  <div class="hero-sub abs">NUTRITION / FITNESS TRAINING</div>
</section>

<section class="welcome abs">
  <h2>WELCOME TO <span>MQ FITNESS</span></h2>
  <p>Mara Quintell builds simple, honest training plans for busy people who want real results. Every program pairs structured workouts with practical nutrition coaching, so you always know what to lift, what to eat and how to keep going. Train at home or in the gym, at your own pace, with support every step of the way.</p>
</section>

<section class="programs abs">
  <article class="program abs" style="left:84px">
    <div class="program-photo" role="img" aria-label="Women training on exercise bikes" style="background:linear-gradient(135deg,#9fc3d8,#e3e9ee)"></div>
    <h3>MY 8 WEEK PROGRAM</h3>
    <p>Eight weeks of guided workouts and meal plans that build strength and steady fat loss.</p>
    <span class="btn">Read More</span>
  </article>
  <article class="program abs" style="left:432px">
    <div class="program-photo" role="img" aria-label="Group fitness class with weights" style="background:linear-gradient(135deg,#5fa9b8,#c9dde0)"></div>
    <h3>TWO 8 WEEK PROGRAM</h3>
    <p>The next phase raises the intensity with new lifts, new meals and fresh weekly goals.</p>
    <span class="btn">Read More</span>
  </article>
  <article class="program abs" style="left:780px">
    <div class="program-photo" role="img" aria-label="Trainer coaching a client with resistance bands" style="background:linear-gradient(135deg,#c98a6a,#e8d4c4)"></div>
    <h3>NUTRITION / FITNESS TRAINING</h3>
    <p>One-to-one online coaching with custom training and nutrition built around your day.</p>
    <span class="btn">Read More</span>
  </article>
</section>

<section class="about abs">
  <div class="about-photo abs" role="img" aria-label="Portrait of Mara outdoors" style="background:linear-gradient(160deg,#7d8a93,#b9a58c)"></div>
  <div class="about-card abs">
    <h2>ABOUT MARA</h2>
    <p>I started training to feel stronger and never looked back. Today I help people everywhere reach their goals with plans that fit real life, including the occasional treat.</p>
    <p>My coaching blends smart lifting, balanced eating and steady habits. No fads, no extremes, just a clear path and someone in your corner who checks in every week.</p>
    <span class="btn">Read More</span>
  </div>
</section>

<section class="blog abs">
  <h2 class="abs">LATEST BLOG</h2>
  <div class="blog-arrows abs">
    <svg width="16" height="16" viewBox="0 0 16 16"><path d="M10 3l-5 5 5 5" stroke="#fff" stroke-width="2" fill="none"/></svg>
    <svg width="16" height="16" viewBox="0 0 16 16"><path d="M6 3l5 5-5 5" stroke="#fff" stroke-width="2" fill="none"/></svg>
  </div>
  <article class="post abs" style="left:84px">
    <div class="post-photo" role="img" aria-label="Smiling group after a workout" style="background:linear-gradient(135deg,#d9b49a,#f1e6dc)"></div>
    <div class="post-body">
      <h3>SIMPLE DUMMY TEXT</h3>
      <div class="post-date">18.05.2013</div>
      <p>Five easy swaps that make weekly meal prep faster and keep your energy high.</p>
      <div class="post-more">Read more »</div>
    </div>
  </article>
  <article class="post abs" style="left:636px">
    <div class="post-photo" role="img" aria-label="Woman stretching on a mat in a gym" style="background:linear-gradient(135deg,#6fa5c4,#d7e4ec)"></div>
    <div class="post-body">
      <h3>SIMPLE DUMMY TEXT</h3>
      <div class="post-date">12.05.2013</div>
      <p>How to plan rest days so your body recovers and your progress keeps climbing.</p>
      <div class="post-more">Read more »</div>
    </div>
  </article>
</section>

<footer class="site-footer abs">
  <div class="footer-links abs">Privacy Policy &nbsp;|&nbsp; Terms of Use &nbsp;|&nbsp; About Us &nbsp;|&nbsp; Sitemap</div>
  <div class="copyright abs">Copyright © 2013. All Rights Reserved</div>
  <div class="footer-right abs">
    <span class="pay-badge"></span>
    <span class="social s1"></span><span class="social s2"></span><span class="social s3"></span><span class="social s4"></span><span class="social s5"></span>
  </div>
</footer>

</body>
</html>
```